innovative investment real estate sales firm

We are a uniquely collabrative firm that seeks to bring a conultative approach to uncovering hidden opportunities for our clients, our website needs to convey our client focused approach. Our firm specializes in the sale of apartment properties in Southern California. We have a team of researchers, transaction coordinators and marketing personal to support our geographically specialized advisers. We need a website that introduces clients to our unique way of better helping them achieve their investment goals.

Target Market(s)

High net worth individuals and families

Industry/Entity Type

Real Estate Agent

Font styles to use
Other font styles liked:
• please use font provided

Requirements
Must have
• Stories of our recent projects
• Features on our people
• email capture for viewing inventory
• content that showcases our unique consultative approach that uncovers unrealized opportunities

```html
<!DOCTYPE html>
<html lang="en">
<head>
<meta charset="utf-8">
<title>Meridale Advisers — Multifamily Properties</title>
<link href="https://fonts.googleapis.com/css2?family=Raleway:wght@500;600;700;800&family=Open+Sans:wght@400;600&family=Oswald:wght@400&display=swap" rel="stylesheet">
<style>
:root{
  --teal:#1a8fab;
  --green:#8cc80a;
  --ink:#2b2b2b;
  --text:#555;
  --light:#f1f1f1;
  --footer:#111;
  --white:#fff;
  --line:#e4e1d6;
  --card:#fffdf3;
}
*{margin:0;padding:0;box-sizing:border-box}
html,body{width:1200px;height:2691px;overflow:hidden;background:var(--white)}
body{position:relative;font-family:"Open Sans",Arial,sans-serif;color:var(--text)}
.abs{position:absolute}
a{color:inherit;text-decoration:none}

/* header */
.header{left:0;top:0;width:1200px;height:129px;background:var(--white)}
.brand{left:100px;top:38px;display:flex;align-items:center;gap:12px}
.brand-mark{width:48px;height:48px;background:var(--ink)}
.brand-name{font-family:"Raleway",sans-serif;font-weight:700;font-size:20px;letter-spacing:1.5px;color:var(--ink);line-height:1;white-space:nowrap}
.phone{left:706px;top:30px;font-size:15px;color:#333;display:flex;align-items:center;gap:10px}
.quote-btn{left:938px;top:22px;width:164px;height:34px;border-radius:17px;background:var(--teal);color:var(--white);font-family:"Raleway",sans-serif;font-weight:700;font-size:12px;display:flex;align-items:center;justify-content:center}
.nav{right:99px;top:85px;display:flex;gap:32px;font-family:"Raleway",sans-serif;font-weight:600;font-size:13px;color:#222}
.nav .active{color:var(--teal)}

/* hero */
.hero{left:0;top:129px;width:1200px;height:556px;background:linear-gradient(180deg,#3e4046 0%,#2a2c31 55%,#4a4a45 100%)}
.hero-title{left:0;top:378px;width:1200px;text-align:center;font-family:"Raleway",sans-serif;font-weight:700;font-size:52px;color:var(--white)}
.hero-sub{left:0;top:443px;width:1200px;text-align:center;font-size:16px;line-height:21px;color:var(--white)}
.dots{left:563px;top:508px;display:flex;gap:8px;align-items:center}
.dot{width:10px;height:10px;border-radius:50%;background:var(--white)}
.dot.on{width:16px;height:16px;border:2px solid var(--white);background:transparent;position:relative}
.dot.on::after{content:"";position:absolute;left:3px;top:3px;width:6px;height:6px;border-radius:50%;background:var(--white)}
.hero-band{left:86px;top:605px;width:1026px;height:80px;background:#8a8a86}

/* features */
.feature{top:617px;width:327px;height:298px;color:var(--white);text-align:center;box-shadow:0 12px 10px -8px rgba(0,0,0,.35)}
.feature.teal{background:var(--teal)}
.feature.green{background:var(--green)}
.feature-icon{margin:24px auto 0;width:90px;height:90px;border:2px solid var(--white);border-radius:50%;display:flex;align-items:center;justify-content:center}
.feature h3{margin-top:22px;font-family:"Raleway",sans-serif;font-weight:700;font-size:18px}
.feature p{margin:14px auto 0;width:280px;font-size:11.5px;line-height:20px}
.feature-more{margin:18px auto 0;width:28px;height:28px;border:1px solid rgba(255,255,255,.8);border-radius:50%;display:flex;align-items:center;justify-content:center}

/* about */
.section-title{left:0;width:1200px;text-align:center;font-family:"Raleway",sans-serif;font-weight:700;font-size:34px;color:var(--ink)}
.about-text{left:160px;top:1062px;width:880px;text-align:center;font-size:12.5px;line-height:21px;color:#444}
.read-more{left:544px;top:1153px;width:112px;height:28px;border-radius:14px;background:var(--teal);color:var(--white);font-family:"Raleway",sans-serif;font-weight:700;font-size:11px;display:flex;align-items:center;justify-content:center;gap:4px}

/* projects */
.projects{left:0;top:1257px;width:1200px;height:508px;background:var(--light)}
.project{top:1390px;width:234px;height:304px;background:var(--card);border:1px solid var(--line)}
.project-photo{margin:4px;height:170px}
.project p{padding:10px 12px 0;font-size:11.5px;line-height:20px;color:#444}
.project-meta{position:absolute;left:0;bottom:0;width:100%;height:44px;border-top:1px solid var(--line);display:flex;font-size:11.5px;color:#333}
.project-meta .loc{flex:1;display:flex;align-items:center;gap:6px;padding-left:10px;border-right:1px solid var(--line)}
.project-meta .price{width:72px;display:flex;align-items:center;justify-content:center}

/* people */
.rule{left:569px;top:1892px;width:62px;height:3px;background:var(--green)}
.person{top:1942px;width:247px;height:298px}
.person-photo{height:238px}
.person-tag{height:60px;background:var(--green);color:var(--white);text-align:center;padding-top:8px}
.person-tag .name{font-family:"Raleway",sans-serif;font-weight:500;font-size:20px;line-height:24px}
.person-tag .role{font-family:"Raleway",sans-serif;font-weight:700;font-size:14px;line-height:20px}

/* footer */
.footer{left:0;top:2331px;width:1200px;height:360px;background:var(--footer);color:var(--white)}
.footer h4{font-family:"Oswald",sans-serif;font-weight:400;font-size:17px;letter-spacing:.3px}
.footer-brand{left:99px;top:2384px;display:flex;align-items:center;gap:10px}
.footer-brand .brand-mark{width:40px;height:40px;background:var(--white)}
.footer-brand .brand-name{color:var(--white);font-size:16px;letter-spacing:1px}
.contact{left:99px;font-size:13px;line-height:20px;display:flex;gap:16px;color:var(--white)}
.contact svg{flex:none;margin-top:2px}
.signup{left:409px;top:2374px;width:290px;color:var(--white)}
.signup p{margin-top:16px;font-size:11.5px;line-height:20px}
.signup .field{margin-top:16px;height:40px;background:var(--white);color:#444;font-size:11px;padding-left:14px;display:flex;align-items:center}
.signup .btn{margin-top:14px;width:100px;height:40px;background:var(--teal);font-family:"Raleway",sans-serif;font-weight:700;font-size:13px;display:flex;align-items:center;justify-content:center}
.links{left:791px;top:2374px;color:var(--white)}
.links ul{list-style:none;margin-top:18px;font-size:12.5px;line-height:24px}
.social{left:1001px;top:2374px;color:var(--white)}
.social ul{list-style:none;margin-top:18px}
.social li{display:flex;align-items:center;gap:10px;height:36px;font-size:14px}
.social .ring{width:26px;height:26px;border:1px solid var(--white);border-radius:50%}
.copyright{left:0;top:2652px;width:1200px;text-align:center;font-size:12.5px;color:var(--white)}
</style>
</head>
<body>

<header class="abs header">
  <div class="abs brand">
    <div class="brand-mark"></div>
    <span class="brand-name">MERIDALE ADVISERS</span>
  </div>
  <div class="abs phone">
    <svg width="18" height="18" viewBox="0 0 24 24"><path fill="#444" d="M6.6 10.8a15 15 0 0 0 6.6 6.6l2.2-2.2c.3-.3.7-.4 1-.2 1.1.4 2.3.6 3.6.6.6 0 1 .4 1 1V20c0 .6-.4 1-1 1A17 17 0 0 1 3 4c0-.6.4-1 1-1h3.5c.6 0 1 .4 1 1 0 1.3.2 2.5.6 3.6.1.3 0 .7-.2 1z"/></svg>
    <span>Phone : 555 0142 7788</span>
  </div>
  <a class="abs quote-btn">GET A FREE QUOTE</a>
  <nav class="abs nav">
    <a class="active">HOME</a><a>ABOUT US</a><a>OUR SERVICES</a><a>PROJECTS</a><a>TEAM</a><a>CONTACT US</a>
  </nav>
</header>

<section class="abs hero" role="img" aria-label="Modern glass office buildings at dusk"></section>
<h1 class="abs hero-title">MERIDALE ADVISERS</h1>
<p class="abs hero-sub">Nemo enim ipsam voluptatem quia voluptas sit aspernatur<br>sed quia consequuntur magni dolores eos</p>
<div class="abs dots"><span class="dot on"></span><span class="dot"></span><span class="dot"></span><span class="dot"></span></div>
<div class="abs hero-band"></div>

<article class="abs feature teal" style="left:99px">
  <div class="feature-icon">
    <svg width="44" height="44" viewBox="0 0 44 44" fill="none" stroke="#fff" stroke-width="2"><path d="M10 20 22 9l12 11M14 17v13h16V17"/><text x="22" y="27" fill="#fff" stroke="none" font-size="10" font-family="Arial" text-anchor="middle">$</text><path d="M4 36h10l6 3h14"/></svg>
  </div>
  <h3>INVESTMENT REAL ESTATE</h3>
  <p>Lorem ipsum dolor sit amet, consectetur adipiscing elit, sed do eiusmod tempor incididunt ut labore et dolore magna aliqua.</p>
  <div class="feature-more"><svg width="12" height="12" viewBox="0 0 12 12" fill="none" stroke="#fff" stroke-width="1.4"><path d="M3 3l6 6M9 4v5H4"/></svg></div>
</article>
<article class="abs feature green" style="left:437px">
  <div class="feature-icon">
    <svg width="40" height="40" viewBox="0 0 40 40" fill="#fff"><path d="M20 7 5 20h4v12h8v-8h6v8h8V20h4z"/></svg>
  </div>
  <h3>SELLING A HOME</h3>
  <p>Lorem ipsum dolor sit amet, consectetur adipiscing elit, sed do eiusmod tempor incididunt ut labore et dolore magna aliqua.</p>
  <div class="feature-more"><svg width="12" height="12" viewBox="0 0 12 12" fill="none" stroke="#fff" stroke-width="1.4"><path d="M3 3l6 6M9 4v5H4"/></svg></div>
</article>
<article class="abs feature teal" style="left:774px">
  <div class="feature-icon">
    <svg width="40" height="40" viewBox="0 0 40 40"><text x="20" y="31" fill="#fff" font-size="32" font-family="Arial" font-weight="700" text-anchor="middle">$</text></svg>
  </div>
  <h3>LOCAL PRICES</h3>
  <p>Lorem ipsum dolor sit amet, consectetur adipiscing elit, sed do eiusmod tempor incididunt ut labore et dolore magna aliqua.</p>
  <div class="feature-more"><svg width="12" height="12" viewBox="0 0 12 12" fill="none" stroke="#fff" stroke-width="1.4"><path d="M3 3l6 6M9 4v5H4"/></svg></div>
</article>

<h2 class="abs section-title" style="top:1002px">ABOUT OUR COMPANY</h2>
<p class="abs about-text">Lorem ipsum dolor sit amet, consectetur adipiscing elit, sed do eiusmod tempor incididunt ut labore et dolore magna aliqua. Ut enim ad minim veniam, quis nostrud exercitation ullamco laboris nisi ut aliquip ex ea commodo consequat. Duis aute irure dolor in reprehenderit in voluptate velit esse cillum dolore eu fugiat nulla pariatur. Excepteur sint occaecat cupidatat non proident, sunt in culpa qui officia deserunt mollit anim</p>
<a class="abs read-more">READ MORE <svg width="10" height="10" viewBox="0 0 10 10"><circle cx="5" cy="5" r="4.5" fill="#fff"/><path d="M4 3l2 2-2 2" stroke="#1a8fab" stroke-width="1.3" fill="none"/></svg></a>

<section class="abs projects"></section>
<h2 class="abs section-title" style="top:1310px">OUR RECENT PROJECTS</h2>

<article class="abs project" style="left:104px">
  <div class="project-photo" role="img" aria-label="Brick and white apartment building under blue sky" style="background:linear-gradient(180deg,#4f86c9 0%,#8fb4de 45%,#b46b4e 75%,#6d8a55 100%)"></div>
  <p>Lorem ipsum dolor sit amet, consetur adipiscing elit, sed do eiusmod tempor incididunt ut labore et</p>
  <div class="project-meta"><span class="loc"><svg width="9" height="12" viewBox="0 0 9 12"><path d="M4.5 0A4.5 4.5 0 0 0 0 4.5C0 8 4.5 12 4.5 12S9 8 9 4.5A4.5 4.5 0 0 0 4.5 0zm0 6.2a1.7 1.7 0 1 1 0-3.4 1.7 1.7 0 0 1 0 3.4z" fill="#333"/></svg>Los Angeles, Califonia</span><span class="price">$370,000</span></div>
</article>
<article class="abs project" style="left:356px">
  <div class="project-photo" role="img" aria-label="Modern white and orange apartment block" style="background:linear-gradient(180deg,#5c8fcf 0%,#c9c6bb 50%,#c9773e 80%,#7b8a5a 100%)"></div>
  <p>Lorem ipsum dolor sit amet, consetur adipiscing elit, sed do eiusmod tempor incididunt ut labore et</p>
  <div class="project-meta"><span class="loc"><svg width="9" height="12" viewBox="0 0 9 12"><path d="M4.5 0A4.5 4.5 0 0 0 0 4.5C0 8 4.5 12 4.5 12S9 8 9 4.5A4.5 4.5 0 0 0 4.5 0zm0 6.2a1.7 1.7 0 1 1 0-3.4 1.7 1.7 0 0 1 0 3.4z" fill="#333"/></svg>Los Angeles, Califonia</span><span class="price">$370,000</span></div>
</article>
<article class="abs project" style="left:612px">
  <div class="project-photo" role="img" aria-label="Colourful apartment buildings with trees" style="background:linear-gradient(180deg,#3d78c4 0%,#9b4a3a 45%,#7c8f9e 70%,#5d7f3b 100%)"></div>
  <p>Lorem ipsum dolor sit amet, consetur adipiscing elit, sed do eiusmod tempor incididunt ut labore et</p>
  <div class="project-meta"><span class="loc"><svg width="9" height="12" viewBox="0 0 9 12"><path d="M4.5 0A4.5 4.5 0 0 0 0 4.5C0 8 4.5 12 4.5 12S9 8 9 4.5A4.5 4.5 0 0 0 4.5 0zm0 6.2a1.7 1.7 0 1 1 0-3.4 1.7 1.7 0 0 1 0 3.4z" fill="#333"/></svg>Los Angeles, Califonia</span><span class="price">$370,000</span></div>
</article>
<article class="abs project" style="left:868px">
  <div class="project-photo" role="img" aria-label="Brick apartment complex with flower beds" style="background:linear-gradient(180deg,#4a86cf 0%,#9fbde0 35%,#a85a42 65%,#5f8a3c 100%)"></div>
  <p>Lorem ipsum dolor sit amet, consetur adipiscing elit, sed do eiusmod tempor incididunt ut labore et</p>
  <div class="project-meta"><span class="loc"><svg width="9" height="12" viewBox="0 0 9 12"><path d="M4.5 0A4.5 4.5 0 0 0 0 4.5C0 8 4.5 12 4.5 12S9 8 9 4.5A4.5 4.5 0 0 0 4.5 0zm0 6.2a1.7 1.7 0 1 1 0-3.4 1.7 1.7 0 0 1 0 3.4z" fill="#333"/></svg>Los Angeles, Califonia</span><span class="price">$370,000</span></div>
</article>

<h2 class="abs section-title" style="top:1830px">OUR PEOPLE</h2>
<div class="abs rule"></div>

<article class="abs person" style="left:99px">
  <div class="person-photo" role="img" aria-label="Portrait of a team member" style="background:linear-gradient(160deg,#8b8680,#5e5650)"></div>
  <div class="person-tag"><div class="name">John Doe</div><div class="role">Senior Manager</div></div>
</article>
<article class="abs person" style="left:350px">
  <div class="person-photo" role="img" aria-label="Portrait of a team member" style="background:linear-gradient(160deg,#9c9a96,#6f625a)"></div>
  <div class="person-tag"><div class="name">John Doe</div><div class="role">Senior Manager</div></div>
</article>
<article class="abs person" style="left:601px">
  <div class="person-photo" role="img" aria-label="Portrait of a team member" style="background:linear-gradient(160deg,#e8e6e3,#c9835e)"></div>
  <div class="person-tag"><div class="name">John Doe</div><div class="role">Senior Manager</div></div>
</article>
<article class="abs person" style="left:852px">
  <div class="person-photo" role="img" aria-label="Portrait of a team member" style="background:linear-gradient(160deg,#777571,#4d4542)"></div>
  <div class="person-tag"><div class="name">John Doe</div><div class="role">Senior Manager</div></div>
</article>

<footer class="abs footer"></footer>
<div class="abs footer-brand"><div class="brand-mark"></div><span class="brand-name">MERIDALE ADVISERS</span></div>
<div class="abs contact" style="top:2458px">
  <svg width="16" height="20" viewBox="0 0 16 20" fill="none" stroke="#fff" stroke-width="1.4"><path d="M8 1a6.5 6.5 0 0 0-6.5 6.5C1.5 12 8 19 8 19s6.5-7 6.5-11.5A6.5 6.5 0 0 0 8 1z"/><circle cx="8" cy="7.5" r="2.3"/></svg>
  <span>Meridale Advisers 4.02, 6th Floor<br>Harbor Tower, Bayview District</span>
</div>
<div class="abs contact" style="top:2510px">
  <svg width="16" height="16" viewBox="0 0 24 24" fill="none" stroke="#fff" stroke-width="1.6"><path d="M6.6 10.8a15 15 0 0 0 6.6 6.6l2.2-2.2c.3-.3.7-.4 1-.2 1.1.4 2.3.6 3.6.6.6 0 1 .4 1 1V20c0 .6-.4 1-1 1A17 17 0 0 1 3 4c0-.6.4-1 1-1h3.5c.6 0 1 .4 1 1 0 1.3.2 2.5.6 3.6.1.3 0 .7-.2 1z"/></svg>
  <span>Phone : &nbsp;1-800-555-0199</span>
</div>
<div class="abs contact" style="top:2544px">
  <svg width="16" height="14" viewBox="0 0 16 12" fill="none" stroke="#fff" stroke-width="1.2"><rect x=".6" y=".6" width="14.8" height="10.8"/><path d="M.6.6 8 7l7.4-6.4"/></svg>
  <span>hello@meridaleadvisers.com</span>
</div>

<div class="abs signup">
  <h4>SIGN UP TO RECEIVE EMAIL</h4>
  <p>Excepteur sint occaecat cupidatat non proident, sunt in culpa qui Nemo enim ipsam voluptatem</p>
  <div class="field">Enter Name</div>
  <div class="btn">SUBSCRIBE</div>
</div>

<div class="abs links">
  <h4>QUICK LINKS</h4>
  <ul><li>Home</li><li>About Us</li><li>Our Recent Projects</li><li>Our People</li><li>Blog</li><li>Contact Us</li></ul>
</div>

<div class="abs social">
  <h4>SOCIAL MEDIA</h4>
  <ul>
    <li><span class="ring"></span>Newsroom</li>
    <li><span class="ring"></span>Updates</li>
    <li><span class="ring"></span>Circles</li>
    <li><span class="ring"></span>Videos</li>
  </ul>
</div>

<p class="abs copyright">Copyright © Meridale Advisers 2017. All rights reserved.</p>

</body>
</html>
```